PowerPoint Corporate Template for Healthcare AI Technology Company

Take logo and create a comprehensive source file for corporate PowerPoint presentation library that provides an array of title/separator slides, graphic presentation options, chart options and text slide options. Utilize the current logo files and provide options on white backgrounds, and knock out options.

Target Market(s)

Pharmaceutical Manufacturers

Font styles to use
Sans Serif

Colors
6b449b
0556a4
33a6d7
0393ce
ffffff
e34197

Requirements
Must have
• Use logos upgraded in files; create an embedded color palette that aligns to the logo; include multiple options for different types of slides including charts; create a bullet point that is the logo in the purple/blue color with white background; incorporate knock out logo version option for separator pages; must include page numbers; use font aligned to logo for text slide options
Nice to have
• Tech looking, data intensive slide options that communicate easily; could be using 3-4 data points per slide
Should not have
• Any logo other than what has been shared

```html
<!DOCTYPE html>
<html lang="en">
<head>
<meta charset="utf-8">
<title>Lumenia Master Slide Library</title>
<link href="https://fonts.googleapis.com/css2?family=Montserrat:wght@300;400;600;700;800&family=Open+Sans:wght@400;600;700&display=swap" rel="stylesheet">
<style>
:root{
  --purple:#6b449b;
  --deep:#55298a;
  --indigo:#4c5bb2;
  --blue:#0556a4;
  --sky:#33a6d7;
  --cyan:#0393ce;
  --pink:#e34197;
  --white:#ffffff;
  --ink:#4a4a55;
  --mute:#8a8a96;
  --line:#d9d9e2;
  --canvas:#e8e8ec;
}
*{box-sizing:border-box}
html,body{margin:0;padding:0}
body{width:1200px;height:4479px;overflow:hidden;background:var(--canvas);font-family:'Open Sans',sans-serif;color:var(--ink);position:relative}
.slide{position:absolute;width:560px;height:313px;background:var(--white);overflow:hidden;box-shadow:0 2px 7px rgba(0,0,0,.16)}
.l{left:24px}.r{left:616px}
.abs{position:absolute}
.band{position:absolute;left:0;top:0;width:490px;height:46px;background:linear-gradient(90deg,#6a3896,#4d5bb1);border-bottom-right-radius:46px}
.band h2{margin:0;color:#fff;font:700 17px/46px 'Montserrat',sans-serif;letter-spacing:.4px;padding-left:50px;text-transform:uppercase}
.pg{position:absolute;right:14px;bottom:8px;font-size:7px;color:#777;letter-spacing:.3px}
.brand{display:flex;align-items:center;gap:8px;font:300 34px 'Montserrat',sans-serif;color:var(--purple)}
.brand .mark{width:32px;height:32px;border:3px solid var(--purple);border-radius:50%}
.brand.knock{color:#fff}.brand.knock .mark{border-color:#fff}
.lorem{font-size:6.6px;line-height:1.6;color:#666;margin:0}
.tiny{font-size:5.6px;line-height:1.5;color:#777;margin:0}
.hdr{font:700 19px 'Montserrat',sans-serif;color:#2e2e38;margin:0}
.hex{width:34px;height:34px;border-radius:50%;background:linear-gradient(135deg,#6b449b,#4c5bb2);border:3px solid #fff;box-shadow:0 0 0 2px #c9bde0;display:flex;align-items:center;justify-content:center}
.hex i{width:13px;height:13px;border:2px solid #fff;border-radius:3px;display:block}
.photo{position:absolute}
.title-lg{font:800 22px/1.15 'Montserrat',sans-serif;margin:0;text-transform:uppercase}
.agenda li{font-size:9.5px;color:#333;margin:0 0 9px;list-style:none;position:relative}
.agenda li::before{content:"";position:absolute;left:-11px;top:4px;width:4px;height:4px;border-radius:50%;background:var(--purple)}
table.data{border-collapse:separate;border-spacing:0 2px;font-size:7px}
table.data th{background:var(--purple);color:#fff;font-weight:600;padding:4px 14px}
table.data td{padding:3px 14px;text-align:center;background:#f3f1f7;color:#444}
table.data td.k{background:var(--purple);color:#fff}
.bar{height:5px;background:#e6e6ec;border-radius:3px;position:relative}
.bar span{position:absolute;left:0;top:0;height:5px;border-radius:3px}
.pj{font:700 7px 'Montserrat',sans-serif;color:var(--deep)}
.num{width:24px;height:24px;background:var(--purple);color:#fff;font:700 10px/24px 'Montserrat',sans-serif;text-align:center}
.cap{font:700 6px 'Montserrat',sans-serif;color:var(--indigo);letter-spacing:.4px;text-transform:uppercase}
.ico{width:30px;height:30px;border-radius:4px;background:var(--purple);display:flex;align-items:center;justify-content:center}
.ico i{width:12px;height:12px;border:2px solid #fff;border-radius:50%;display:block}
.card{position:absolute;background:#fff;border-radius:10px;box-shadow:0 3px 12px rgba(80,60,130,.22)}
</style>
</head>
<body>

<!-- Row 1 -->
<section class="slide l" style="top:30px">
  <div class="brand abs" style="left:52px;top:130px"><span class="mark"></span>Lumenia</div>
  <div class="abs" style="right:4px;top:120px;transform:rotate(-90deg);font-size:5px;color:#aaa;letter-spacing:1px">www.lumenia.com</div>
</section>

<section class="slide r" style="top:30px">
  <div class="brand abs" style="left:14px;top:14px;font-size:26px;gap:6px"><span class="mark" style="width:24px;height:24px;border-width:2px"></span>Lumenia</div>
  <div class="abs" style="left:14px;top:140px;width:2px;height:60px;background:var(--purple)"></div>
  <h1 class="abs title-lg" style="left:28px;top:150px;font-size:19px;color:var(--purple)">Lumenia Master Slide</h1>
  <div class="abs" style="left:28px;top:178px;font-size:6.5px;letter-spacing:1.5px;color:#777">PRESENTATION TEMPLATE</div>
  <div class="abs" style="left:14px;bottom:10px;font-size:6px;color:#555">June 2020</div>
  <div class="photo" role="img" aria-label="Grayscale photo of hands resting on a laptop keyboard" style="right:0;top:0;width:300px;height:313px;background:linear-gradient(120deg,rgba(255,255,255,0) 0%,#e6e6e6 25%,#b9b9b9 70%,#8d8d8d 100%)"></div>
</section>

<!-- Row 2 -->
<section class="slide l" style="top:370px;background:linear-gradient(100deg,#1a1d3a 0%,#2a2450 35%,#6a3896 45%,#4d5bb1 100%)">
  <div class="photo" role="img" aria-label="Glowing blue illustration of a DNA strand on a dark background" style="left:45px;top:48px;width:160px;height:220px;border-radius:26px;background:radial-gradient(circle at 50% 50%,#3b86d6 0%,#1c3a78 40%,#0b1230 80%)"></div>
  <h1 class="abs title-lg" style="right:32px;top:48px;color:#fff;text-align:right;font-size:20px">Lumenia Master Slide<br>Presentation</h1>
  <div class="abs" style="right:32px;top:110px;color:#fff;font-size:6.5px;font-weight:600">June 2020</div>
</section>

<section class="slide r" style="top:370px;background:linear-gradient(180deg,#6a3896 0%,#4d5bb1 32%,#4d5bb1 70%,#6a3896 100%)">
  <div class="abs" style="left:0;top:82px;width:560px;height:150px;background:#e8e2f0"></div>
  <div class="abs" style="left:14px;top:82px;width:2px;height:150px;background:var(--purple)"></div>
  <h1 class="abs title-lg" style="left:36px;top:124px;color:var(--purple);font-size:21px">Master Slide<br>Presentation</h1>
  <div class="abs" style="left:36px;top:178px;font-size:6.5px;letter-spacing:1.5px;color:#777">MODERN TEMPLATE</div>
  <div class="brand abs" style="right:28px;top:134px;font-size:30px"><span class="mark" style="width:28px;height:28px"></span>Lumenia</div>
  <div class="abs" style="right:14px;bottom:10px;font-size:6px;color:#fff">June 2020</div>
</section>

<!-- Row 3 -->
<section class="slide l" style="top:713px">
  <div class="band"><h2>Agenda</h2></div>
  <ul class="agenda abs" style="left:54px;top:80px;margin:0;padding:0">
    <li>Introduction</li><li>About Us</li><li>Welcome Message</li><li>Portfolio</li><li>Our Services</li><li>Team</li><li>Company values</li><li>Info graphic Charts</li><li>Contact Us</li>
  </ul>
  <div class="pg">PAGE | 5</div>
</section>

<section class="slide r" style="top:713px">
  <div class="band"><h2>About Us</h2></div>
  <div class="abs" style="left:36px;top:90px;width:300px">
    <p class="lorem">Lorem ipsum dolor sit amet, consectetuer adipiscing elit, sed diam nonummy nibh euismod tincidunt ut laoreet dolore magna aliquam erat volutpat. Ut wisi enim ad minim veniam, quis nostrud exerci tation ullamcorper suscipit lobortis nisl ut aliquip ex ea commodo consequat. Duis autem vel eum iriure dolor in hendrerit in vulputate velit esse molestie consequat, vel illum dolore eu feugiat nulla facilisis.</p>
    <p class="lorem" style="margin-top:10px">Lorem ipsum dolor sit amet, cons ectetuer adipiscing elit, sed diam nonummy nibh euismod tincidunt ut laoreet dolore magna aliquam erat volutpat. Ut wisi enim ad minim veniam, quis nostrud exerci tation ullamcorper suscipit lobortis nisl ut aliquip ex ea commodo consequat.</p>
  </div>
  <div class="card" style="left:340px;top:70px;width:200px;height:200px"></div>
  <div class="abs" style="left:326px;top:100px;display:flex;flex-direction:column;gap:28px">
    <div style="display:flex;align-items:center;gap:14px"><div class="hex"><i></i></div><span style="font-size:8px;color:var(--indigo);font-weight:600">Lorem ipsum dolor</span></div>
    <div style="display:flex;align-items:center;gap:14px"><div class="hex"><i></i></div><span style="font-size:8px;color:var(--indigo);font-weight:600">Lorem ipsum dolor</span></div>
    <div style="display:flex;align-items:center;gap:14px"><div class="hex"><i></i></div><span style="font-size:8px;color:var(--indigo);font-weight:600">Lorem ipsum dolor</span></div>
  </div>
  <div class="pg">PAGE | 6</div>
</section>

<!-- Row 4 -->
<section class="slide l" style="top:1056px;background:linear-gradient(160deg,#6a3896,#4d5bb1)">
  <div class="abs" style="left:140px;top:0;width:420px;height:313px;background:#fff;border-top-left-radius:40px;border-bottom-left-radius:40px"></div>
  <h2 class="abs" style="left:18px;top:148px;margin:0;color:#fff;font:800 16px/1.1 'Montserrat',sans-serif">OUR<br>Process</h2>
  <div class="abs" style="left:150px;top:72px;display:flex;gap:25px">
    <div style="display:flex;flex-direction:column;align-items:center;gap:6px"><div class="hex" style="width:48px;height:48px"><i style="width:18px;height:18px;border-radius:50%"></i></div><div style="width:52px;height:52px;border:1px solid #ccc;border-radius:4px;font-size:6px;color:#888;text-align:center;padding-top:8px">Lorem<br>ipsum<br>dolor</div><div style="width:1px;height:36px;background:#aaa"></div></div>
    <div style="display:flex;flex-direction:column;align-items:center;gap:6px"><div class="hex" style="width:48px;height:48px;background:var(--indigo)"><i style="width:18px;height:18px"></i></div><div style="width:52px;height:52px;border:1px solid #ccc;border-radius:4px;font-size:6px;color:#888;text-align:center;padding-top:8px">Lorem<br>ipsum<br>dolor</div><div style="width:1px;height:36px;background:#aaa"></div></div>
    <div style="display:flex;flex-direction:column;align-items:center;gap:6px"><div class="hex" style="width:48px;height:48px"><i style="width:18px;height:18px;border-radius:50%"></i></div><div style="width:52px;height:52px;border:1px solid #ccc;border-radius:4px;font-size:6px;color:#888;text-align:center;padding-top:8px">Lorem<br>ipsum<br>dolor</div><div style="width:1px;height:36px;background:#aaa"></div></div>
    <div style="display:flex;flex-direction:column;align-items:center;gap:6px"><div class="hex" style="width:48px;height:48px;background:var(--indigo)"><i style="width:18px;height:18px"></i></div><div style="width:52px;height:52px;border:1px solid #ccc;border-radius:4px;font-size:6px;color:#888;text-align:center;padding-top:8px">Lorem<br>ipsum<br>dolor</div><div style="width:1px;height:36px;background:#aaa"></div></div>
    <div style="display:flex;flex-direction:column;align-items:center;gap:6px"><div class="hex" style="width:48px;height:48px"><i style="width:18px;height:18px;border-radius:50%"></i></div><div style="width:52px;height:52px;border:1px solid #ccc;border-radius:4px;font-size:6px;color:#888;text-align:center;padding-top:8px">Lorem<br>ipsum<br>dolor</div><div style="width:1px;height:36px;background:#aaa"></div></div>
  </div>
  <svg class="abs" style="left:160px;top:260px" width="360" height="12" viewBox="0 0 360 12"><line x1="0" y1="6" x2="352" y2="6" stroke="#bbb" stroke-width="2"/><path d="M350 1 L358 6 L350 11" fill="none" stroke="#bbb" stroke-width="2"/></svg>
  <div class="pg">PAGE | 7</div>
</section>

<section class="slide r" style="top:1056px">
  <div class="band"><h2 style="text-transform:none">Example Slide</h2></div>
  <div class="photo" role="img" aria-label="Magnifying glass over an AI chip icon" style="left:40px;top:80px;width:150px;height:150px;border-radius:50%;background:radial-gradient(circle,#ffffff 55%,#c8c8cc 57%,#b5b5ba 66%,#ffffff 67%)"></div>
  <div class="abs" style="left:255px;top:96px;width:270px"><p class="lorem" style="text-align:justify">Lorem ipsum dolor sit amet, consectetuer adipiscing elit, sed diam nonummy nibh euismod tincidunt ut laoreet dolore magna aliquam erat volutpat. Ut wisi enim ad minim veniam, quis nostrud exerci tation ullamcorper suscipit lobortis nisl ut aliquip ex ea commodo consequat. Duis autem vel eum iriure dolor in hendrerit in vulputate velit esse molestie consequat, vel illum dolore eu feugiat nulla facilisis.</p></div>
  <div class="abs" style="left:290px;top:230px;background:var(--purple);color:#fff;font:700 6.5px/16px 'Montserrat',sans-serif;letter-spacing:1px;padding:0 18px;border-radius:9px">LEARN MORE</div>
  <div class="pg">PAGE | 8</div>
</section>

<!-- Row 5 -->
<section class="slide l" style="top:1396px">
  <div class="photo" role="img" aria-label="Close-up photo of a microscope lens framed by a purple circle" style="left:-100px;top:-40px;width:330px;height:393px;border-radius:50%;background:radial-gradient(circle at 40% 55%,#3a3a44 0%,#141418 55%,#141418 88%);box-shadow:0 0 0 16px #6a3896"></div>
  <h2 class="abs" style="left:22px;top:120px;margin:0;color:#fff;font:700 20px/1.05 'Montserrat',sans-serif">Example<br>Slide</h2>
  <div class="abs" style="left:22px;top:168px;width:44px;height:2px;background:#fff"></div>
  <div class="abs" style="left:280px;top:28px;display:flex;align-items:center;gap:14px"><div class="hex"><i></i></div><span style="font-size:9px;color:#444">Lorem ipsum</span></div>
  <div class="abs" style="left:310px;top:102px;display:flex;align-items:center;gap:14px"><div class="hex"><i style="border-radius:50%"></i></div><span style="font-size:9px;color:#444">Lorem ipsum</span></div>
  <div class="abs" style="left:310px;top:176px;display:flex;align-items:center;gap:14px"><div class="hex"><i></i></div><span style="font-size:9px;color:#444">Lorem ipsum</span></div>
  <div class="abs" style="left:280px;top:250px;display:flex;align-items:center;gap:14px"><div class="hex"><i style="border-radius:50%"></i></div><span style="font-size:9px;color:#444">Lorem ipsum</span></div>
  <div class="pg">PAGE | 9</div>
</section>

<section class="slide r" style="top:1396px;background:linear-gradient(160deg,#6a3896,#4d5bb1)">
  <h2 class="abs" style="left:22px;top:16px;margin:0;color:#fff;font:700 17px 'Montserrat',sans-serif">LINE CHART</h2>
  <div class="abs" style="left:140px;top:60px;width:420px;height:253px;background:#fff;border-top-left-radius:40px"></div>
  <svg class="abs" style="left:180px;top:100px" width="350" height="180" viewBox="0 0 350 180">
    <g font-size="5" fill="#888" font-family="Open Sans,sans-serif">
      <text x="0" y="10">120</text><text x="0" y="36">100</text><text x="0" y="62">80</text><text x="0" y="88">60</text><text x="0" y="114">40</text><text x="0" y="140">20</text><text x="4" y="166">0</text>
    </g>
    <line x1="16" y1="164" x2="340" y2="164" stroke="#ccc" stroke-width=".6"/>
    <g>
      <rect x="24" y="34" width="14" height="130" fill="#6b2f8f"/><rect x="39" y="46" width="14" height="118" fill="#3c4fb0"/>
      <rect x="69" y="46" width="14" height="118" fill="#6b2f8f"/><rect x="84" y="60" width="14" height="104" fill="#3c4fb0"/>
      <rect x="114" y="34" width="14" height="130" fill="#6b2f8f"/><rect x="129" y="86" width="14" height="78" fill="#3c4fb0"/>
      <rect x="159" y="34" width="14" height="130" fill="#6b2f8f"/><rect x="174" y="74" width="14" height="90" fill="#3c4fb0"/>
      <rect x="204" y="34" width="14" height="130" fill="#6b2f8f"/><rect x="219" y="46" width="14" height="118" fill="#3c4fb0"/>
      <rect x="249" y="60" width="14" height="104" fill="#6b2f8f"/><rect x="264" y="74" width="14" height="90" fill="#3c4fb0"/>
      <rect x="294" y="34" width="14" height="130" fill="#6b2f8f"/><rect x="309" y="86" width="14" height="78" fill="#3c4fb0"/>
    </g>
    <g font-size="5" fill="#888" font-family="Open Sans,sans-serif">
      <text x="32" y="174">Jan</text><text x="77" y="174">Mar</text><text x="122" y="174">Fe</text><text x="167" y="174">Ah</text><text x="212" y="174">Ag</text><text x="257" y="174">Fr</text><text x="302" y="174">Ju</text>
    </g>
  </svg>
  <div class="pg" style="color:#777">PAGE | 10</div>
</section>

<!-- Row 6 -->
<section class="slide l" style="top:1739px">
  <div class="band"><h2>XY Chart</h2></div>
  <svg class="abs" style="left:30px;top:95px" width="300" height="170" viewBox="0 0 300 170">
    <g font-size="5" fill="#888" font-family="Open Sans,sans-serif"><text x="0" y="12">120</text><text x="0" y="36">100</text><text x="0" y="60">80</text><text x="0" y="84">60</text><text x="0" y="108">40</text><text x="0" y="132">20</text><text x="4" y="156">0</text></g>
    <line x1="16" y1="154" x2="295" y2="154" stroke="#ccc" stroke-width=".6"/>
    <path d="M40 60 C70 20, 90 110, 130 70 S190 20, 220 60 S270 80, 290 60" fill="none" stroke="#4c5bb2" stroke-width="1.4"/>
    <path d="M40 40 C70 30, 95 20, 115 60 S150 110, 180 50 S250 40, 290 80" fill="none" stroke="#6b449b" stroke-width="1.4"/>
    <g fill="#888" font-size="5" font-family="Open Sans,sans-serif"><text x="40" y="164">0</text><text x="80" y="164">1</text><text x="120" y="164">2</text><text x="160" y="164">3</text><text x="200" y="164">4</text><text x="240" y="164">5</text><text x="280" y="164">6</text></g>
  </svg>
  <div class="abs" style="left:400px;top:104px;width:135px">
    <div style="font:700 8px 'Montserrat',sans-serif;color:#333;margin-bottom:6px">LOREM IPSUM</div>
    <p class="lorem" style="text-align:justify">Lorem ipsum dolor sit amet, consectetuer adipiscing elit, sed diam nonummy nibh euismod tincidunt ut laoreet dolore magna aliquam erat volutpat. Ut wisi enim ad minim veniam, quis nostrud exerci tation ullamcorper suscipit lobortis nisl ut aliquip ex ea commodo consequat.</p>
  </div>
  <div class="pg">PAGE | 11</div>
</section>

<section class="slide r" style="top:1739px">
  <div class="abs" style="right:0;top:0;width:140px;height:313px;background:linear-gradient(160deg,#6a3896,#4d5bb1);border-top-left-radius:40px"></div>
  <h2 class="abs hdr" style="left:46px;top:26px">Example Slide</h2>
  <div class="abs" style="left:46px;top:56px;width:30px;height:2px;background:var(--purple)"></div>
  <div class="card" style="left:46px;top:110px;width:130px;height:165px"></div>
  <div class="card" style="left:214px;top:110px;width:130px;height:165px"></div>
  <div class="card" style="left:378px;top:110px;width:130px;height:165px"></div>
  <div class="abs" style="left:93px;top:88px"><div class="hex"><i></i></div></div>
  <div class="abs" style="left:261px;top:88px"><div class="hex"><i style="border-radius:50%"></i></div></div>
  <div class="abs" style="left:425px;top:88px"><div class="hex"><i></i></div></div>
  <div class="abs" style="left:56px;top:136px;width:110px;text-align:center"><div style="font:700 10px 'Montserrat',sans-serif;color:#333;margin-bottom:10px">Lorem ipsum</div><p class="tiny">Lorem ipsum dolor sit amet, consectetuer adipiscing elit, sed diam nonummy nibh euismod tincidunt ut laoreet dolore magna aliquam erat volutpat.</p></div>
  <div class="abs" style="left:224px;top:136px;width:110px;text-align:center"><div style="font:700 10px 'Montserrat',sans-serif;color:#333;margin-bottom:10px">Lorem ipsum</div><p class="tiny">Lorem ipsum dolor sit amet, consectetuer adipiscing elit, sed diam nonummy nibh euismod tincidunt ut laoreet dolore magna aliquam erat volutpat.</p></div>
  <div class="abs" style="left:388px;top:136px;width:110px;text-align:center"><div style="font:700 10px 'Montserrat',sans-serif;color:#333;margin-bottom:10px">Lorem ipsum</div><p class="tiny">Lorem ipsum dolor sit amet, consectetuer adipiscing elit, sed diam nonummy nibh euismod tincidunt ut laoreet dolore magna aliquam erat volutpat.</p></div>
  <div class="pg" style="left:8px;right:auto">PAGE | 12</div>
</section>

<!-- Row 7 -->
<section class="slide l" style="top:2082px">
  <div class="band"><h2>Pie Chart</h2></div>
  <div class="abs" style="left:150px;top:88px;font-size:6px;color:var(--indigo)">Your Text here</div>
  <svg class="abs" style="left:55px;top:100px" width="150" height="150" viewBox="25 15 90 90">
    <path d="M70 60 L70 15 A45 45 0 0 1 114.2 51.6Z" fill="#5b8fd6"/>
    <path d="M70 60 L114.2 51.6 A45 45 0 0 1 96.5 96.4Z" fill="#4a5cb3"/>
    <path d="M70 60 L96.5 96.4 A45 45 0 1 1 70 15Z" fill="#6b2f8f"/>
    <g fill="#fff" font-size="6" font-family="Open Sans,sans-serif"><text x="78" y="36">22%</text><text x="90" y="68">18%</text><text x="37" y="68">60%</text></g>
  </svg>
  <div class="abs" style="left:212px;top:138px;width:52px;height:44px;background:#6d6d78;color:#fff;font-size:9px;text-align:center;line-height:44px">10%</div>
  <div class="abs" style="left:212px;top:182px;width:52px;height:34px;background:#c9c9d1;color:#444;font-size:9px;text-align:center;line-height:34px">8%</div>
  <div class="abs" style="left:140px;top:252px;font-size:5px;color:#777">● 1st Qtr ● 2nd Qtr ● 3rd Qtr ● 4th Qtr</div>
  <div class="abs" style="left:340px;top:96px;width:180px">
    <div style="font:700 7px 'Montserrat',sans-serif;color:var(--deep)">Insert title here</div><p class="tiny" style="margin:2px 0 9px">There are many variations of passages of lorem ipsum available, but the majority have suffered alteration in some form, act</p>
    <div style="font:700 7px 'Montserrat',sans-serif;color:var(--indigo)">Insert title here</div><p class="tiny" style="margin:2px 0 9px">There are many variations of passages of lorem ipsum available, but the majority have suffered alteration in some form, act</p>
    <div style="font:700 7px 'Montserrat',sans-serif;color:#777">Insert title here</div><p class="tiny" style="margin:2px 0 0">There are many variations of passages of lorem ipsum available, but the majority have suffered alteration in some form, act</p>
  </div>
  <div class="pg">PAGE | 13</div>
</section>

<section class="slide r" style="top:2082px">
  <div class="band"><h2>Infographic &amp; Mockups</h2></div>
  <div class="abs" style="left:42px;top:68px;width:106px;height:216px;border:2px solid #bbb;border-radius:14px;background:#fff"></div>
  <div class="abs" style="left:50px;top:88px;width:90px;height:168px;border:1px solid #e0e0e0;background:#fafafa"></div>
  <div class="brand abs" style="left:58px;top:112px;font-size:14px;gap:4px"><span class="mark" style="width:12px;height:12px;border-width:1.5px"></span>Lumenia</div>
  <div class="abs" style="left:58px;top:226px;width:76px;font-size:5.5px;color:#777;text-align:center">Add your text/<br>picture here and<br>send it to back</div>
  <div class="abs" style="left:176px;top:100px;width:150px;display:flex;flex-direction:column;gap:24px">
    <p class="tiny">Lorem ipsum is simply dummy text of the printing and typesetting industry</p>
    <p class="tiny">Lorem ipsum is simply dummy text of the printing and typesetting industry</p>
    <p class="tiny">Lorem ipsum is simply dummy text of the printing and typesetting industry</p>
    <p class="tiny">Lorem ipsum is simply dummy text of the printing and typesetting industry</p>
  </div>
  <svg class="abs" style="left:352px;top:86px" width="180" height="180" viewBox="0 0 180 180">
    <circle cx="90" cy="90" r="66" fill="none" stroke="#e34197" stroke-width="44"/>
    <circle cx="90" cy="90" r="66" fill="none" stroke="#6b2f8f" stroke-width="44" stroke-dasharray="51.84 51.84"/>
    <circle cx="90" cy="90" r="44" fill="#fff"/>
    <text x="90" y="88" text-anchor="middle" font-size="7" font-weight="700" fill="#333" font-family="Open Sans,sans-serif">Add your text</text>
    <text x="90" y="97" text-anchor="middle" font-size="7" font-weight="700" fill="#333" font-family="Open Sans,sans-serif">here</text>
  </svg>
  <div class="pg">PAGE | 14</div>
</section>

<!-- Row 8 -->
<section class="slide l" style="top:2423px">
  <div class="band"><h2>Tables</h2></div>
  <table class="data abs" style="left:70px;top:100px">
    <tr><th style="background:transparent"></th><th>Title here</th><th>Numbers</th><th>Value</th><th>Brand</th><th>Quality</th></tr>
    <tr><td class="k">Content type</td><td>Example one</td><td>3</td><td>10</td><td>New</td><td>15%</td></tr>
    <tr><td class="k">Content type</td><td>Example two</td><td>6</td><td>45</td><td>New</td><td>60%</td></tr>
    <tr><td class="k">Content type</td><td>Example three</td><td>6</td><td>67</td><td>New</td><td>67%</td></tr>
    <tr><td class="k">Content type</td><td>Example four</td><td>9</td><td>94</td><td>New</td><td>22%</td></tr>
    <tr><td class="k">Content type</td><td>Example five</td><td>2</td><td>50</td><td>New</td><td>15%</td></tr>
    <tr><td class="k">Content type</td><td>Example six</td><td>1</td><td>90</td><td>New</td><td>09%</td></tr>
    <tr><td class="k">Content type</td><td>Example seven</td><td>5</td><td>31</td><td>New</td><td>10%</td></tr>
  </table>
  <div class="pg">PAGE | 15</div>
</section>

<section class="slide r" style="top:2423px">
  <div class="photo" role="img" aria-label="Abstract blue digital network of glowing particles" style="inset:0;background:radial-gradient(ellipse at 75% 50%,#5f8fe8 0%,#1f4cb4 35%,#1a2f88 70%,#141d5a 100%)"></div>
  <div class="abs" style="left:66px;top:68px;width:320px;height:190px;border:1px solid rgba(255,255,255,.7);border-radius:10px"></div>
  <div class="abs" style="left:40px;top:118px;width:300px;height:172px;background:rgba(90,110,200,.55)"></div>
  <h2 class="abs" style="left:82px;top:208px;margin:0;color:#fff;font:700 24px 'Montserrat',sans-serif">Section 01</h2>
</section>

<!-- Row 9 -->
<section class="slide l" style="top:2765px">
  <div class="band"><h2>Project Charts</h2></div>
  <svg class="abs" style="left:36px;top:84px" width="76" height="76" viewBox="0 0 76 76"><circle cx="38" cy="38" r="32" fill="none" stroke="#e9e9ee" stroke-width="6"/><circle cx="38" cy="38" r="32" fill="none" stroke="#6b2f8f" stroke-width="6" stroke-dasharray="146.8 201" transform="rotate(-90 38 38)"/><text x="38" y="44" text-anchor="middle" font-size="18" font-family="Montserrat,sans-serif" fill="#55298a">73%</text></svg>
  <svg class="abs" style="left:36px;top:180px" width="76" height="76" viewBox="0 0 76 76"><circle cx="38" cy="38" r="32" fill="none" stroke="#e9e9ee" stroke-width="6"/><circle cx="38" cy="38" r="32" fill="none" stroke="#e34197" stroke-width="6" stroke-dasharray="100.5 201" transform="rotate(-90 38 38)"/><text x="38" y="44" text-anchor="middle" font-size="18" font-family="Montserrat,sans-serif" fill="#55298a">50%</text></svg>
  <div class="abs" style="left:132px;top:110px;width:100px"><div class="pj">PROJECT 01</div><p class="tiny">Lorem ipsum is simply dummy text of the printing and typesetting industry</p></div>
  <div class="abs" style="left:132px;top:206px;width:100px"><div class="pj">PROJECT 02</div><p class="tiny">Lorem ipsum is simply dummy text of the printing and typesetting industry</p></div>
  <div class="abs" style="left:272px;top:84px;width:236px;display:flex;flex-direction:column;gap:17px">
    <div><div style="display:flex;justify-content:space-between"><span class="pj">PROJECT 03</span><span class="tiny">32%</span></div><div class="bar"><span style="width:32%;background:#e34197"></span></div></div>
    <div><div style="display:flex;justify-content:space-between"><span class="pj">PROJECT 04</span><span class="tiny">72%</span></div><div class="bar"><span style="width:72%;background:#4c5bb2"></span></div></div>
    <div><div style="display:flex;justify-content:space-between"><span class="pj">PROJECT 05</span><span class="tiny">52%</span></div><div class="bar"><span style="width:52%;background:#6b2f8f"></span></div></div>
    <div><div style="display:flex;justify-content:space-between"><span class="pj">PROJECT 06</span><span class="tiny">12%</span></div><div class="bar"><span style="width:12%;background:#e34197"></span></div></div>
    <div><div style="display:flex;justify-content:space-between"><span class="pj">PROJECT 07</span><span class="tiny">60%</span></div><div class="bar"><span style="width:60%;background:#6b2f8f"></span></div></div>
  </div>
  <div class="pg">PAGE | 17</div>
</section>

<section class="slide r" style="top:2765px">
  <div class="abs" style="left:0;top:0;width:560px;height:150px;background:linear-gradient(160deg,#6a3896,#4d5bb1);border-bottom-right-radius:60px"></div>
  <h2 class="abs" style="left:0;width:560px;top:28px;margin:0;text-align:center;color:#fff;font:700 18px 'Montserrat',sans-serif">OUR TEAM</h2>
  <div class="photo" role="img" aria-label="Portrait photo of team member" style="left:108px;top:82px;width:82px;height:82px;border-radius:50%;border:3px solid #fff;background:linear-gradient(160deg,#d8d8dc,#8d8d95)"></div>
  <div class="photo" role="img" aria-label="Portrait photo of team member" style="left:239px;top:82px;width:82px;height:82px;border-radius:50%;border:3px solid #fff;background:linear-gradient(160deg,#cfcfd3,#6f6f78)"></div>
  <div class="photo" role="img" aria-label="Portrait photo of team member" style="left:370px;top:82px;width:82px;height:82px;border-radius:50%;border:3px solid #fff;background:linear-gradient(160deg,#e0e0e4,#a1a1aa)"></div>
  <div class="abs" style="left:84px;top:176px;width:130px;text-align:center"><div style="font:700 7.5px 'Montserrat',sans-serif;color:var(--indigo)">Example Name</div><div style="font-size:6px;color:#999;margin-bottom:5px">CEO</div><p class="tiny">There are many variations of passages of lorem ipsum available, but the majority have suffered alteration</p><div style="margin-top:8px;font-size:7px;color:#999;letter-spacing:3px">○○○</div></div>
  <div class="abs" style="left:215px;top:176px;width:130px;text-align:center"><div style="font:700 7.5px 'Montserrat',sans-serif;color:var(--indigo)">Example Name</div><div style="font-size:6px;color:#999;margin-bottom:5px">Member</div><p class="tiny">There are many variations of passages of lorem ipsum available, but the majority have suffered alteration</p><div style="margin-top:8px;font-size:7px;color:#999;letter-spacing:3px">○○○</div></div>
  <div class="abs" style="left:346px;top:176px;width:130px;text-align:center"><div style="font:700 7.5px 'Montserrat',sans-serif;color:var(--indigo)">Example Name</div><div style="font-size:6px;color:#999;margin-bottom:5px">Member</div><p class="tiny">There are many variations of passages of lorem ipsum available, but the majority have suffered alteration</p><div style="margin-top:8px;font-size:7px;color:#999;letter-spacing:3px">○○○</div></div>
  <div class="pg">PAGE | 18</div>
</section>

<!-- Row 10 -->
<section class="slide l" style="top:3108px">
  <div class="band"><h2>Analysis</h2></div>
  <svg class="abs" style="left:200px;top:90px" width="160" height="170" viewBox="0 0 160 170">
    <circle cx="80" cy="42" r="30" fill="#6b2f8f"/><circle cx="80" cy="128" r="30" fill="#6b2f8f"/>
    <circle cx="37" cy="85" r="30" fill="#4c5bb2"/><circle cx="123" cy="85" r="30" fill="#4c5bb2"/>
    <circle cx="80" cy="42" r="18" fill="#fff"/><circle cx="80" cy="128" r="18" fill="#fff"/><circle cx="37" cy="85" r="18" fill="#fff"/><circle cx="123" cy="85" r="18" fill="#fff"/>
    <circle cx="80" cy="85" r="14" fill="#4c5bb2"/><rect x="74" y="79" width="12" height="12" rx="2" fill="none" stroke="#fff" stroke-width="1.6"/>
    <g font-family="Montserrat,sans-serif" font-size="16" font-weight="600" fill="#333" text-anchor="middle"><text x="80" y="48">S</text><text x="123" y="91">W</text><text x="37" y="91">T</text><text x="80" y="134">O</text></g>
  </svg>
  <div class="abs" style="left:20px;top:112px;width:175px;text-align:right"><div class="cap" style="color:var(--deep)">Strength</div><p class="tiny">Lorem ipsum dolor sit amet, consectetuer adipiscing elit, sed diam nonummy nibh euismod tincidunt ut laoreet dolore magna aliquam erat</p></div>
  <div class="abs" style="left:366px;top:112px;width:175px"><div class="cap" style="color:var(--deep)">Weakness</div><p class="tiny">Lorem ipsum dolor sit amet, consectetuer adipiscing elit, sed diam nonummy nibh euismod tincidunt ut laoreet dolore magna aliquam erat</p></div>
  <div class="abs" style="left:20px;top:228px;width:175px;text-align:right"><div class="cap">Threat</div><p class="tiny">Lorem ipsum dolor sit amet, consectetuer adipiscing elit, sed diam nonummy nibh euismod tincidunt ut laoreet dolore magna aliquam erat</p></div>
  <div class="abs" style="left:366px;top:228px;width:175px"><div class="cap">Opportunity</div><p class="tiny">Lorem ipsum dolor sit amet, consectetuer adipiscing elit, sed diam nonummy nibh euismod tincidunt ut laoreet dolore magna aliquam erat</p></div>
  <div class="pg">PAGE | 19</div>
</section>

<section class="slide r" style="top:3108px">
  <h2 class="abs" style="left:0;width:560px;top:18px;margin:0;text-align:center;color:var(--indigo);font:700 17px 'Montserrat',sans-serif">TEXT INFORMATION</h2>
  <div class="abs" style="left:30px;top:72px;display:grid;grid-template-columns:240px 240px;column-gap:20px;row-gap:22px">
    <div style="display:flex;gap:12px"><div class="num">1</div><div><div class="cap">Text information</div><p class="tiny">Lorem ipsum dolor sit amet, consectetuer adipiscing elit, sed diam nonummy nibh euismod tincidunt ut laoreet dolore magn</p></div></div>
    <div style="display:flex;gap:12px"><div class="num">4</div><div><div class="cap">Text information</div><p class="tiny">Lorem ipsum dolor sit amet, consectetuer adipiscing elit, sed diam nonummy nibh euismod tincidunt ut laoreet dolore magn</p></div></div>
    <div style="display:flex;gap:12px"><div class="num">2</div><div><div class="cap">Text information</div><p class="tiny">Lorem ipsum dolor sit amet, consectetuer adipiscing elit, sed diam nonummy nibh euismod tincidunt ut laoreet dolore magn</p></div></div>
    <div style="display:flex;gap:12px"><div class="num">5</div><div><div class="cap">Text information</div><p class="tiny">Lorem ipsum dolor sit amet, consectetuer adipiscing elit, sed diam nonummy nibh euismod tincidunt ut laoreet dolore magn</p></div></div>
    <div style="display:flex;gap:12px"><div class="num">3</div><div><div class="cap">Text information</div><p class="tiny">Lorem ipsum dolor sit amet, consectetuer adipiscing elit, sed diam nonummy nibh euismod tincidunt ut laoreet dolore magn</p></div></div>
    <div style="display:flex;gap:12px"><div class="num">6</div><div><div class="cap">Text information</div><p class="tiny">Lorem ipsum dolor sit amet, consectetuer adipiscing elit, sed diam nonummy nibh euismod tincidunt ut laoreet dolore magn</p></div></div>
  </div>
</section>

<!-- Row 11 -->
<section class="slide l" style="top:3450px">
  <div class="band"><h2>Infographic</h2></div>
  <svg class="abs" style="left:80px;top:70px" width="400" height="230" viewBox="0 0 400 230">
    <g stroke="#aaa" stroke-width=".8" fill="none">
      <path d="M120 40 H165 L185 75"/><path d="M120 120 H152"/><path d="M120 200 H165 L185 165"/>
      <path d="M280 40 H235 L215 75"/><path d="M280 120 H248"/><path d="M280 200 H235 L215 165"/>
    </g>
    <circle cx="200" cy="120" r="50" fill="#fff" stroke="#6b2f8f" stroke-width="2"/>
    <circle cx="165" cy="162" r="4" fill="#e34197"/><circle cx="235" cy="78" r="4" fill="#e34197"/>
  </svg>
  <div class="brand abs" style="left:253px;top:180px;font-size:15px;gap:4px"><span class="mark" style="width:12px;height:12px;border-width:1.5px"></span>Lumenia</div>
  <div class="abs" style="left:86px;top:92px;display:flex;gap:10px"><div class="ico"><i></i></div><div style="width:72px"><div class="pj">LOREM IPSUM</div><p class="tiny">Lorem ipsum dolor sit amet, consectetuer adipiscing</p></div></div>
  <div class="abs" style="left:86px;top:170px;display:flex;gap:10px"><div class="ico"><i></i></div><div style="width:72px"><div class="pj">LOREM IPSUM</div><p class="tiny">Lorem ipsum dolor sit amet, consectetuer adipiscing</p></div></div>
  <div class="abs" style="left:86px;top:248px;display:flex;gap:10px"><div class="ico"><i></i></div><div style="width:72px"><div class="pj">LOREM IPSUM</div><p class="tiny">Lorem ipsum dolor sit amet, consectetuer adipiscing</p></div></div>
  <div class="abs" style="left:362px;top:92px;display:flex;gap:10px"><div style="width:72px"><div class="pj">LOREM IPSUM</div><p class="tiny">Lorem ipsum dolor sit amet, consectetuer adipiscing</p></div><div class="ico"><i></i></div></div>
  <div class="abs" style="left:362px;top:170px;display:flex;gap:10px"><div style="width:72px"><div class="pj">LOREM IPSUM</div><p class="tiny">Lorem ipsum dolor sit amet, consectetuer adipiscing</p></div><div class="ico"><i></i></div></div>
  <div class="abs" style="left:362px;top:248px;display:flex;gap:10px"><div style="width:72px"><div class="pj">LOREM IPSUM</div><p class="tiny">Lorem ipsum dolor sit amet, consectetuer adipiscing</p></div><div class="ico"><i></i></div></div>
  <div class="pg">PAGE | 21</div>
</section>

<section class="slide r" style="top:3450px;background:linear-gradient(120deg,#3a4aa8,#2d3f9c 50%,#3a55b8)">
  <div class="photo" role="img" aria-label="Glowing digital head with AI lettering among technology icons" style="left:300px;top:20px;width:250px;height:280px;border-radius:50%;background:radial-gradient(circle,#8fb0f0 0%,#4e6fcf 40%,rgba(58,74,168,0) 72%)"></div>
  <div class="abs" style="left:26px;top:24px;width:170px;display:flex;flex-direction:column;gap:24px">
    <div><div style="font:700 9px 'Montserrat',sans-serif;color:#fff;margin-bottom:5px">Lorem ipsum</div><p class="tiny" style="color:#d9defa">Lorem ipsum dolor sit amet, consectetuer adipiscing elit, sed diam nonummy nibh euismod tincidunt ut laoreet dolore magna aliquam erat volutpat.</p></div>
    <div><div style="font:700 9px 'Montserrat',sans-serif;color:#fff;margin-bottom:5px">Lorem ipsum</div><p class="tiny" style="color:#d9defa">Lorem ipsum dolor sit amet, consectetuer adipiscing elit, sed diam nonummy nibh euismod tincidunt ut laoreet dolore magna aliquam erat volutpat.</p></div>
    <div><div style="font:700 9px 'Montserrat',sans-serif;color:#fff;margin-bottom:5px">Lorem ipsum</div><p class="tiny" style="color:#d9defa">Lorem ipsum dolor sit amet, consectetuer adipiscing elit, sed diam nonummy nibh euismod tincidunt ut laoreet dolore magna aliquam erat volutpat.</p></div>
  </div>
</section>

<!-- Row 12 -->
<section class="slide l" style="top:3793px">
  <div class="band"><h2>Service Locations</h2></div>
  <div class="photo" role="img" aria-label="World map with highlighted service regions and location pins" style="left:170px;top:70px;width:370px;height:210px;border-radius:8px;background:radial-gradient(ellipse at 50% 50%,#e6e3ef 0%,#f3f2f7 70%,#ffffff 100%)"></div>
  <div class="abs" style="left:100px;top:80px;width:28px;height:28px;border-radius:50%;background:var(--purple)"></div>
  <div class="abs" style="left:26px;top:118px;width:120px"><div style="font:700 7px 'Montserrat',sans-serif;color:var(--indigo)">Main US</div><p class="tiny">Lorem ipsum dolor sit amet, consectetuer adipiscing elit</p></div>
  <div class="abs" style="left:26px;top:150px;width:120px;display:flex;flex-direction:column;gap:10px">
    <div><div style="display:flex;justify-content:space-between"><span class="pj" style="font-size:5.5px">PROJECT 01</span><span class="tiny">50%</span></div><div class="bar" style="height:3px"><span style="width:50%;height:3px;background:#e34197"></span></div></div>
    <div><div style="display:flex;justify-content:space-between"><span class="pj" style="font-size:5.5px">PROJECT 02</span><span class="tiny">30%</span></div><div class="bar" style="height:3px"><span style="width:30%;height:3px;background:#6b2f8f"></span></div></div>
  </div>
  <div class="abs" style="left:26px;top:210px;font:700 7px 'Montserrat',sans-serif;color:#333">Shipping</div>
  <div class="pg">PAGE | 23</div>
</section>

<section class="slide r" style="top:3793px">
  <h2 class="abs hdr" style="left:46px;top:26px">Example Slide</h2>
  <div class="abs" style="left:46px;top:56px;width:30px;height:2px;background:var(--purple)"></div>
  <svg class="abs" style="left:0;top:0" width="560" height="313" viewBox="0 0 560 313">
    <g stroke="#6d74c4" stroke-width="1" fill="none">
      <path d="M88 150 H180 V120 H220"/><path d="M88 156 H180 V185 H220"/>
      <path d="M340 130 H390 V100 H450"/><path d="M340 170 H390 V200 H450"/><path d="M400 150 H470"/>
      <path d="M492 20 V130"/><path d="M500 20 V130"/><path d="M508 20 V130"/><path d="M492 175 V300"/><path d="M500 175 V300"/><path d="M508 175 V300"/>
    </g>
    <rect x="480" y="132" width="38" height="40" fill="#fff" stroke="#4c5bb2" stroke-width="2"/>
    <text x="499" y="157" text-anchor="middle" font-family="Montserrat,sans-serif" font-weight="700" font-size="13" fill="#4c5bb2">AI</text>
  </svg>
  <div class="abs" style="left:30px;top:124px;width:60px;height:60px;border-radius:50%;border:1px solid #999;display:flex;align-items:center;justify-content:center;font:300 11px 'Montserrat',sans-serif;color:var(--purple)">Lumenia</div>
  <div class="photo" role="img" aria-label="Brain illustration split in blue and purple halves" style="left:220px;top:90px;width:125px;height:120px;border-radius:50%;background:linear-gradient(90deg,#4c5bb2 0%,#4c5bb2 49%,#fff 49%,#fff 51%,#6b449b 51%)"></div>
  <div class="abs" style="left:390px;top:28px;width:150px;text-align:right"><div style="font:700 7px 'Montserrat',sans-serif;color:var(--pink)">Lorem ipsum</div><p class="tiny">Lorem ipsum dolor sit amet, consectetuer adipiscing elit, sed diam nonummy nibh euismod</p></div>
  <div class="abs" style="left:30px;top:216px;width:90px"><div style="font:700 7px 'Montserrat',sans-serif;color:var(--indigo)">Lorem ipsum</div><p class="tiny">Lorem ipsum dolor sit amet, consectetuer adipiscing elit, sed diam nonummy nibh euismod</p></div>
  <div class="abs" style="left:206px;top:226px;width:72px;text-align:center"><div style="font:700 7px 'Montserrat',sans-serif;color:var(--indigo)">Lorem ipsum</div><p class="tiny">Lorem ipsum dolor sit amet, consectetuer adipiscing elit, sed diam nonummy</p></div>
  <div class="abs" style="left:290px;top:226px;width:72px;text-align:center"><div style="font:700 7px 'Montserrat',sans-serif;color:var(--pink)">Lorem ipsum</div><p class="tiny">Lorem ipsum dolor sit amet, consectetuer adipiscing elit, sed diam nonummy</p></div>
</section>

<!-- Row 13 -->
<section class="slide l" style="top:4135px">
  <h2 class="abs" style="left:0;width:560px;top:20px;margin:0;text-align:center;color:#444;font:700 14px 'Montserrat',sans-serif">Free editable vector icon links available</h2>
  <div class="photo" role="img" aria-label="Grid of editable purple line icons for healthcare, technology and business" style="left:28px;top:58px;width:504px;height:236px;border-radius:6px;background:repeating-linear-gradient(90deg,#f1edf7 0 14px,#ffffff 14px 20px),linear-gradient(180deg,#ece6f4,#e7e9f6)"></div>
</section>

<section class="slide r" style="top:4135px;background:linear-gradient(160deg,#6a3896,#4d5bb1)">
  <div class="brand knock abs" style="left:200px;top:28px;font-size:60px;gap:14px"><span class="mark" style="width:58px;height:58px;border-width:4px"></span>Lumenia</div>
  <h2 class="abs" style="left:32px;top:118px;margin:0;color:#fff;font:600 16px 'Montserrat',sans-serif">Get in Touch</h2>
  <div class="abs" style="left:40px;top:158px;display:flex;flex-direction:column;gap:16px;color:#fff;font-size:7px">
    <div style="display:flex;align-items:center;gap:14px"><svg width="12" height="12" viewBox="0 0 12 12"><circle cx="6" cy="6" r="5" fill="none" stroke="#fff"/><path d="M1 6H11M6 1C3 4 3 8 6 11M6 1C9 4 9 8 6 11" fill="none" stroke="#fff" stroke-width=".7"/></svg>www.yourwebsite.com</div>
    <div style="display:flex;align-items:center;gap:14px"><svg width="12" height="12" viewBox="0 0 12 12"><path d="M2 1 L4.5 1 L5.5 3.5 L4 4.5 C4.8 6.5 5.5 7.2 7.5 8 L8.5 6.5 L11 7.5 L11 10 C6 11 1 6 2 1Z" fill="none" stroke="#fff"/></svg>+1 234 567 890</div>
    <div style="display:flex;align-items:center;gap:14px"><svg width="12" height="12" viewBox="0 0 12 12"><rect x="1" y="2.5" width="10" height="7" fill="none" stroke="#fff"/><path d="M1 2.5 L6 7 L11 2.5" fill="none" stroke="#fff"/></svg>info@yourmail.com</div>
    <div style="display:flex;align-items:center;gap:14px"><svg width="12" height="12" viewBox="0 0 12 12"><path d="M6 11 C2 6.5 2 5 2 4.5 A4 4 0 0 1 10 4.5 C10 5 10 6.5 6 11Z" fill="none" stroke="#fff"/><circle cx="6" cy="4.5" r="1.5" fill="#fff"/></svg>Add Your Address, street, road , here</div>
  </div>
</section>

</body>
</html>
```